New modern business card design

To design a brand new business card that's clean & modern in terms of layout.
I have attached our company logo and also basic information regarding what is needed on the card that also needs to be editable.

Target Market(s)

motor trade

Contact Information for Business Card

logo, name, title, tel, mob, email, address, www, all information is in the word.doc file

Requirements
Must have
• white background
Nice to have
• Nice clean font

```html
<!DOCTYPE html>
<html lang="en">
<head>
<meta charset="utf-8">
<title>Northgate Fixings — Business Card</title>
<link rel="stylesheet" href="https://fonts.googleapis.com/css2?family=Oswald:wght@600&family=Work+Sans:wght@400;500&display=swap">
<style>
  :root {
    --bg: #e4e4e6;
    --card: #ffffff;
    --card-edge: #d2d2d4;
    --pattern-light: #f4f4f5;
    --pattern-mid: #e2e2e4;
    --pattern-dark: #c9c9cc;
    --text-strong: #1c1c1d;
    --text-body: #2b2b2c;
    --text-muted: #6a6a6c;
    --divider: #b5b5b8;
    --brand-blue: #1d7fc4;
  }
  * { margin: 0; padding: 0; box-sizing: border-box; }
  html, body { width: 1200px; height: 900px; overflow: hidden; }
  body {
    background: var(--bg);
    font-family: "Work Sans", Arial, sans-serif;
    position: relative;
  }
  .card {
    position: absolute;
    left: 250px;
    width: 700px;
    height: 400px;
    background: var(--card);
    border: 1px solid var(--card-edge);
  }
  .card--front { top: 40px; }
  .card--back { top: 470px; }

  .front-pattern {
    position: absolute;
    inset: 0;
    background: linear-gradient(100deg, var(--pattern-light) 0%, var(--pattern-mid) 50%, var(--pattern-dark) 100%);
  }
  .wordmark {
    position: absolute;
    left: 470px;
    top: 258px;
    display: flex;
    align-items: center;
    gap: 10px;
    font-weight: 500;
    font-size: 26px;
    color: var(--brand-blue);
    letter-spacing: 0.5px;
  }
  .wordmark__square {
    width: 18px;
    height: 18px;
    background: var(--brand-blue);
  }

  .identity {
    position: absolute;
    right: 390px;
    top: 128px;
    text-align right;
    text-align: right;
  }
  .identity__name {
    font-family: "Oswald", "Arial Narrow", sans-serif;
    font-weight: 600;
    font-size: 40px;
    letter-spacing: 0.5px;
    color: var(--text-strong);
    text-transform: uppercase;
    line-height: 1;
  }
  .identity__title {
    font-size: 17px;
    color: var(--text-muted);
    margin-top: 6px;
  }
  .divider {
    position: absolute;
    left: 332px;
    top: 125px;
    width: 1px;
    height: 80px;
    background: var(--divider);
  }
  .contact {
    position: absolute;
    left: 352px;
    top: 120px;
    list-style: none;
  }
  .contact__item {
    display: flex;
    align-items: center;
    gap: 12px;
    font-size: 18px;
    color: var(--text-body);
    line-height: 22px;
  }
  .contact__icon { width: 12px; height: 12px; flex: none; }
  .address {
    position: absolute;
    left: 60px;
    bottom: 60px;
    font-size: 21px;
    color: var(--text-body);
  }
</style>
</head>
<body>
  <section class="card card--front">
    <div class="front-pattern" role="img" aria-label="Repeating brand monogram pattern in graded greys"></div>
    <div class="wordmark"><span class="wordmark__square"></span>Northgate</div>
  </section>

  <section class="card card--back">
    <div class="identity">
      <h1 class="identity__name">Daniel Hurst</h1>
      <p class="identity__title">General Manager</p>
    </div>
    <div class="divider"></div>
    <ul class="contact">
      <li class="contact__item">
        <svg class="contact__icon" viewBox="0 0 12 12"><path d="M2 1h2l1 3-1.5 1a6 6 0 0 0 3.5 3.5L8 7l3 1v2a1 1 0 0 1-1 1A9 9 0 0 1 1 2a1 1 0 0 1 1-1z" fill="var(--text-muted)"/></svg>
        0113 480 2215
      </li>
      <li class="contact__item">
        <svg class="contact__icon" viewBox="0 0 12 12"><rect x="3" y="0.5" width="6" height="11" rx="1" fill="none" stroke="var(--text-muted)"/><circle cx="6" cy="9.5" r="0.7" fill="var(--text-muted)"/></svg>
        07700 900 418
      </li>
      <li class="contact__item">
        <svg class="contact__icon" viewBox="0 0 12 12"><rect x="0.5" y="2.5" width="11" height="7" fill="none" stroke="var(--text-muted)"/><path d="M0.5 2.5 6 7l5.5-4.5" fill="none" stroke="var(--text-muted)"/></svg>
        dhurst@northgate-fix.co.uk
      </li>
      <li class="contact__item">
        <svg class="contact__icon" viewBox="0 0 12 12"><circle cx="6" cy="6" r="5.3" fill="none" stroke="var(--text-muted)"/><path d="M0.7 6h10.6M6 0.7c-2.5 3-2.5 7.6 0 10.6M6 0.7c2.5 3 2.5 7.6 0 10.6" fill="none" stroke="var(--text-muted)"/></svg>
        www.northgate-fix.co.uk
      </li>
    </ul>
    <p class="address">Carlton Road Denby, Leeds LS9 4QT</p>
  </section>
</body>
</html>
```